HARLOWE FREIGHT & PLANT HIRE NEEDS A FLYER

WE NEED A FLYER FOR OUR COMPANY <br/>WE SPECIALISE IN ROAD BUILDING AND MAINTENANCE, GENERAL EARTHWORK DAM REPAIRS & DESILTING, FENCE CLEARING, FIRE BREAKS, GRAVEL SOURCE AND DELIVERY GENERAL FREIGHT STEEL HAY LICK AND MCHINERY. <br/><br/>I HAVE UPLOAD A FILE THAT I LIKE AND WOULD LIKE SOMETHING THE SAME IF POSSIBLE. AND LOGO TO GO WITH IT.

```html
<!DOCTYPE html>
<html lang="en">
<head>
<meta charset="utf-8">
<title>Harlowe Freight &amp; Plant Hire Flyer</title>
<link rel="stylesheet" href="https://fonts.googleapis.com/css2?family=Oswald:wght@400;500&display=swap">
<style>
  :root {
    --charcoal: #38393a;
    --charcoal-deep: #303132;
    --amber: #fbbc1a;
    --paper: #ffffff;
    --paper-shade: #e9e9e9;
    --hatch: #d9d9d9;
    --ink: #1f1f1f;
  }
  * { margin: 0; padding: 0; box-sizing: border-box; }
  html, body { width: 900px; height: 1200px; overflow: hidden; background: #f2f2f2; }
  .flyer {
    position: relative;
    width: 900px;
    height: 1200px;
    overflow: hidden;
    font-family: "Oswald", "Arial Narrow", sans-serif;
    background: radial-gradient(ellipse at 50% 40%, var(--paper) 45%, var(--paper-shade) 100%);
  }
  .backdrop { position: absolute; inset: 0; width: 900px; height: 1200px; }
  .top-band {
    position: absolute; left: 0; top: 0; width: 900px; height: 88px;
    background: var(--charcoal);
    display: flex; align-items: center; justify-content: center;
  }
  .tagline { color: var(--amber); font-size: 37px; font-weight: 400; letter-spacing: 0.5px; }
  .brand {
    position: absolute; left: 0; top: 170px; width: 900px;
    text-align: center; color: var(--charcoal); font-weight: 500; line-height: 1;
  }
  .brand-name { font-size: 104px; letter-spacing: 3px; }
  .brand-trade { font-size: 56px; margin-top: 12px; letter-spacing: 1px; }
  .brand-entity { font-size: 36px; margin-top: 10px; letter-spacing: 2px; }
  .section { position: absolute; left: 66px; }
  .section-title { color: var(--amber); font-size: 33px; font-weight: 500; line-height: 1; margin-bottom: 16px; }
  .section-list { color: var(--paper); font-size: 29px; font-weight: 400; line-height: 44.5px; white-space: nowrap; }
  .services { top: 492px; }
  .machinery { top: 776px; }
  .contact {
    position: absolute; right: 30px; top: 1038px; width: 460px;
    color: var(--ink); text-align: center;
  }
  .contact-names { font-size: 33px; font-weight: 400; line-height: 1; }
  .contact-phone {
    display: flex; align-items: center; justify-content: center; gap: 10px;
    font-size: 48px; font-weight: 500; line-height: 1; margin-top: 14px;
  }
  .contact-phone svg { width: 42px; height: 42px; }
  .contact-email { font-size: 27px; line-height: 1; margin-top: 16px; text-align: right; }
  .contact-email .label { font-size: 20px; }
</style>
</head>
<body>
<div class="flyer">
  <svg class="backdrop" viewBox="0 0 900 1200" aria-hidden="true">
    <polygon class="dark-field" points="0,336 900,506 900,1200 0,1200" fill="var(--charcoal)"/>
    <polygon class="hatch-field" points="42,1200 383,1071 496,1200" fill="var(--hatch)"/>
    <polygon class="amber-field" points="383,1071 900,904 900,1200 496,1200" fill="var(--amber)"/>
  </svg>

  <header class="top-band">
    <p class="tagline">FOR ALL YOU FREIGHT AND PLANT HIRE NEEDS!</p>
  </header>

  <div class="brand">
    <div class="brand-name">HARLOWE</div>
    <div class="brand-trade">FREIGHT &amp; PLANT HIRE</div>
    <div class="brand-entity">PTY LTD</div>
  </div>

  <section class="section services">
    <h2 class="section-title">SPECIALISING IN:</h2>
    <div class="section-list">
      <div>ROAD BUILDING AND MAINTENANCE • GENERAL</div>
      <div>EARTHWORKS &nbsp;• DAM REPAIRS &amp; DESILTING &nbsp;• FENCE</div>
      <div>CLEARING • &nbsp;FIRE BREAKS &nbsp;• &nbsp;GRAVEL SOURCE &amp; DELIVERY</div>
      <div>GENERAL FREIGHT • STEEL • &nbsp;LICK • HAY &nbsp;• MACHINERY</div>
    </div>
  </section>

  <section class="section machinery">
    <h2 class="section-title">CURRENT MACHINERY AVAILABLE:</h2>
    <div class="section-list">
      <div>GRADER • LOADER &amp; STICK RAKE &nbsp;• ROLLERS</div>
      <div>DOZER &nbsp;• WATER TRUCKS • SIDE TIPPERS • PRIME</div>
      <div>MOVERS • FORKLIFT &nbsp;• SKID STEER LOADER • FLAT</div>
      <div>TOPS • DROP DECK</div>
    </div>
  </section>

  <address class="contact" style="font-style:normal">
    <div class="contact-names">DEAN &amp; MARLA CORRICK</div>
    <div class="contact-phone">
      <svg viewBox="0 0 24 24" aria-hidden="true">
        <path fill="var(--ink)" d="M6.6 10.8a15.1 15.1 0 0 0 6.6 6.6l2.2-2.2a1 1 0 0 1 1-.25 11.4 11.4 0 0 0 3.6.57 1 1 0 0 1 1 1V20a1 1 0 0 1-1 1A17 17 0 0 1 3 4a1 1 0 0 1 1-1h3.5a1 1 0 0 1 1 1c0 1.25.2 2.45.57 3.57a1 1 0 0 1-.25 1z"/>
        <path fill="none" stroke="var(--ink)" stroke-width="1.6" stroke-linecap="round" d="M14 3.5a7 7 0 0 1 6.5 6.5M14 7a3.5 3.5 0 0 1 3 3"/>
      </svg>
      <span>0438205917</span>
    </div>
    <div class="contact-email"><span class="label">EMAIL:</span> marlacorrick@mailbox.com</div>
  </address>
</div>
</body>
</html>
```